Brovin Terra LLC - Excavation Contractor in Idaho

Wordpress website, visually appealing....Company is Veteran owned business, owner SGT Darrell Oswick NQAF, anything from laser grading to cleaning up your property we do various Skidsteer work and are always buying new attachments to do more jobs. Services include: excavation, grading, snow plowing, demolition and cleanup, fence post hole drilling, trenching.

Target Market(s)

Contractors and Home owners needing projects completed

Industry/Entity Type

Construction

Number of Pages Required

3 page

Font styles to use
Sans Serif

Requirements
Must have
• Site visually appealing and easy to navigate.
Nice to have
• Maybe bold colors?

```html
<!DOCTYPE html>
<html lang="en">
<head>
<meta charset="utf-8">
<title>Brovin Terra LLC – Excavation Contractor in Idaho</title>
<link rel="stylesheet" href="https://fonts.googleapis.com/css2?family=Raleway:wght@400;500;600;700;800&display=swap">
<style>
:root{
  --red:#d0201b;
  --black:#121212;
  --white:#ffffff;
  --text:#6b6b6b;
  --ink:#111111;
  --hero-a:#8c8a7e;
  --hero-b:#4c4a40;
  --hero-c:#6b5a3e;
}
*{margin:0;padding:0;box-sizing:border-box}
html,body{width:1200px;height:3745px;overflow:hidden}
body{font-family:"Raleway",Arial,sans-serif;background:var(--white);color:var(--ink);position:relative}
.abs{position:absolute}
.center-text{text-align:center}
.btn{position:absolute;display:flex;align-items:center;justify-content:center;background:var(--red);color:var(--white);font-weight:700;font-size:15px;text-transform:uppercase;letter-spacing:.2px}
.btn-outline{background:var(--white);color:var(--ink);border:2px solid var(--red)}

/* header */
.site-header{position:absolute;left:0;top:0;width:1200px;height:95px;background:var(--black)}
.brand{position:absolute;left:116px;top:30px;display:flex;align-items:center;gap:10px;color:var(--white);font-weight:800;font-size:21px;line-height:34px;text-transform:uppercase}
.brand-mark{width:14px;height:14px;background:var(--red)}
.main-nav{position:absolute;top:40px;left:0;font-size:14px;font-weight:700;color:var(--white);text-transform:uppercase}
.main-nav span{position:absolute;white-space:nowrap}
.main-nav .active{color:var(--red)}
.nav-pointer{position:absolute;left:382px;top:85px}
.quote-btn{position:absolute;left:964px;top:0;width:236px;height:95px;background:var(--red);color:var(--white);font-weight:800;font-size:19px;display:flex;align-items:center;justify-content:center;text-transform:uppercase}

/* hero */
.hero-art{position:absolute;left:0;top:95px}
.hero-title{position:absolute;left:0;width:1200px;top:305px;font-size:50px;font-weight:800;color:var(--white);text-transform:uppercase}
.hero-sub{position:absolute;left:320px;width:560px;top:378px;font-size:18px;font-weight:700;line-height:30px;color:var(--white)}

/* dark bands */
.dark-band{position:absolute;left:0;width:1200px;background:var(--black)}
.section-title{position:absolute;left:0;width:1200px;font-weight:700;text-transform:uppercase}
.on-dark{color:var(--white)}
.about-text{position:absolute;left:145px;width:910px;top:926px;font-size:14.5px;line-height:26.5px;color:var(--white);font-weight:500}

/* services */
.service-card{position:absolute;top:1344px;width:313px;height:372px;background:var(--white);box-shadow:0 2px 8px rgba(0,0,0,.18)}
.service-photo{position:absolute;left:6px;top:6px;width:301px;height:195px}
.service-name{position:absolute;left:0;width:100%;top:226px;font-size:15px;font-weight:700;text-transform:uppercase}
.service-text{position:absolute;left:12px;right:12px;top:259px;font-size:13.5px;line-height:24px;color:var(--text)}

/* why choose */
.value-card{position:absolute;top:2167px;width:231px;height:258px;background:var(--white)}
.value-icon{position:absolute;left:88px;top:22px;width:56px;height:56px}
.value-name{position:absolute;left:0;width:100%;top:104px;font-size:17px;font-weight:600;text-transform:uppercase}
.value-rule{position:absolute;left:98px;top:131px;width:35px;height:2px;background:var(--red)}
.value-text{position:absolute;left:8px;right:8px;top:150px;font-size:13px;line-height:23px;color:var(--text)}

/* projects */
.project-photo{position:absolute}

/* footer */
.footer-brand{position:absolute;left:116px;top:3488px;display:flex;align-items:center;gap:10px;color:var(--white);font-weight:800;font-size:27px;text-transform:uppercase}
.social-box{position:absolute;top:3580px;width:33px;height:33px;background:var(--white);display:flex;align-items:center;justify-content:center}
.social-box i{width:13px;height:13px;background:var(--red);display:block}
.footer-heading{position:absolute;top:3444px;font-size:17px;font-weight:700;color:var(--white);text-transform:uppercase}
.footer-list{position:absolute;list-style:none;color:var(--white);font-size:15.5px;font-weight:500}
.footer-list li{position:relative;height:27.7px;line-height:22px;padding-left:34px}
.footer-list li svg{position:absolute;left:0;top:4px}
.contact-line{position:absolute;left:919px;color:var(--white);font-size:15.5px;font-weight:500;line-height:26px}
.contact-icon{position:absolute;left:889px}
.footer-rule{position:absolute;left:112px;top:3687px;width:976px;height:1px;background:#444}
.copyright{position:absolute;left:0;width:1200px;top:3704px;font-size:12px;color:var(--white)}
.copyright b{font-weight:800}
.copyright .accent{color:var(--red)}
</style>
</head>
<body>

<!-- Header -->
<header class="site-header">
  <div class="brand"><span class="brand-mark"></span>Brovin Terra LLC</div>
  <nav class="main-nav">
    <span class="active" style="left:372px">Home</span>
    <span style="left:435px">About Us</span>
    <span style="left:531px">Our Services</span>
    <span style="left:656px">Projects</span>
    <span style="left:749px">Blog</span>
    <span style="left:810px">Contact Us</span>
  </nav>
  <svg class="nav-pointer" width="34" height="10" viewBox="0 0 34 10"><rect x="0" y="7" width="34" height="3" fill="#d0201b"/><polygon points="11,7 17,1 23,7" fill="#d0201b"/></svg>
  <div class="quote-btn">Request a Qoute</div>
</header>

<!-- Hero -->
<svg class="hero-art" width="1200" height="700" viewBox="0 0 1200 700">
  <defs>
    <linearGradient id="heroFill" x1="0" y1="0" x2="1" y2="1">
      <stop offset="0" stop-color="#9a9c8e"/>
      <stop offset="0.5" stop-color="#5a5548"/>
      <stop offset="1" stop-color="#6e5c40"/>
    </linearGradient>
  </defs>
  <rect x="0" y="0" width="1200" height="700" fill="#121212"/>
  <polygon points="0,0 1200,0 1200,530 600,670 0,530" fill="url(#heroFill)" role="img" aria-label="Photo of a tracked compact loader with an auger attachment on a dirt job site"/>
  <polygon points="0,530 600,670 1200,530 1200,540 600,690 0,540" fill="#d0201b"/>
</svg>
<h1 class="hero-title center-text">Welcome to Brovin Terra LLC</h1>
<p class="hero-sub center-text">Lorem ipsum dolor sit amet, consectetur adipiscing elit, sed do tempor incididunt ut laborea.</p>
<div class="btn" style="left:522px;top:460px;width:156px;height:49px">Get Started</div>

<!-- About -->
<div class="dark-band" style="top:795px;height:357px"></div>
<h2 class="section-title on-dark center-text" style="top:845px;font-size:45px">About Brovin Terra LLC</h2>
<p class="about-text center-text">Lorem ipsum dolor sit amet, consectetur adipiscing elit, sed do eiusmod tempor incididunt ut labore et dolore magna aliqua. Ut enim ad minim veniam, quis nostrud exercitation ullamco laboris nisi ut aliquip ex ea commodo consequat. Duis aute irure dolor in reprehe nderit in voluptate velit esse cillum dolore eu fugiat nulla pariatur.</p>
<div class="btn" style="left:523px;top:1043px;width:154px;height:49px">Learn More</div>

<!-- Services -->
<h2 class="section-title center-text" style="top:1236px;font-size:45px">Our Services</h2>

<article class="service-card" style="left:112px">
  <div class="service-photo" style="background:linear-gradient(160deg,#b9c2cc,#5d6a4a 55%,#4a3a2a)" role="img" aria-label="Photo of a tracked loader pushing soil for excavation"></div>
  <h3 class="service-name center-text">Excavation</h3>
  <p class="service-text center-text">Lorem ipsum dolor sit amet, consectetur a dipiscing elit, sed do eiusmod tempor inc aeidunt labore dolorea.</p>
</article>
<article class="service-card" style="left:444px">
  <div class="service-photo" style="background:linear-gradient(160deg,#aab4c0,#3f5a9c 50%,#7a6650)" role="img" aria-label="Photo of a loader clearing debris beside a blue roll-off dumpster"></div>
  <h3 class="service-name center-text">Demolition &amp; Cleanup</h3>
  <p class="service-text center-text">Lorem ipsum dolor sit amet, consectetur a dipiscing elit, sed do eiusmod tempor inc aeidunt labore dolorea.</p>
</article>
<article class="service-card" style="left:775px">
  <div class="service-photo" style="background:linear-gradient(160deg,#b7c3cf,#8c8a6a 50%,#2e2e2e)" role="img" aria-label="Photo of a tracked loader with a wide bucket attachment in a field"></div>
  <h3 class="service-name center-text">Trenching</h3>
  <p class="service-text center-text">Lorem ipsum dolor sit amet, consectetur a dipiscing elit, sed do eiusmod tempor inc aeidunt labore dolorea.</p>
</article>
<div class="btn" style="left:204px;top:1692px;width:129px;height:48px">Learn More</div>
<div class="btn" style="left:536px;top:1692px;width:129px;height:48px">Learn More</div>
<div class="btn" style="left:867px;top:1692px;width:129px;height:48px">Learn More</div>
<div class="btn btn-outline" style="left:506px;top:1787px;width:187px;height:50px">View All Services</div>

<!-- Why choose -->
<svg class="abs" style="left:0;top:1860px" width="1200" height="640" viewBox="0 0 1200 640">
  <rect x="0" y="0" width="1200" height="640" fill="#121212"/>
  <polygon points="0,22 600,148 1200,22 1200,30 600,170 0,30" fill="#d0201b"/>
</svg>
<h2 class="section-title on-dark center-text" style="top:2076px;font-size:38px">Why Choose Brovin Terra LLC</h2>

<article class="value-card" style="left:112px">
  <svg class="value-icon" viewBox="0 0 56 56" fill="#d0201b">
    <circle cx="22" cy="12" r="8"/>
    <path d="M8 44 v-12 a10 10 0 0 1 10-10 h8 a10 10 0 0 1 8 4 v18z"/>
    <circle cx="40" cy="32" r="9"/><circle cx="40" cy="32" r="4" fill="#fff"/>
    <rect x="38" y="20" width="4" height="4"/><rect x="38" y="40" width="4" height="4"/><rect x="28" y="30" width="4" height="4"/><rect x="48" y="30" width="4" height="4"/>
    <rect x="4" y="46" width="34" height="4"/>
  </svg>
  <h3 class="value-name center-text">Leadership</h3><div class="value-rule"></div>
  <p class="value-text center-text">Lorem ipsum dolor sit amet acoe ctetur adipiscing elit, sed deiuio dtempaor incididunt ut laboet magna aliqua.</p>
</article>
<article class="value-card" style="left:361px">
  <svg class="value-icon" viewBox="0 0 56 56" fill="#d0201b">
    <path d="M4 52 V16 h14 V6 h20 v10 h14 v36z"/>
    <g fill="#fff"><rect x="22" y="12" width="4" height="5"/><rect x="30" y="12" width="4" height="5"/><rect x="22" y="22" width="4" height="5"/><rect x="30" y="22" width="4" height="5"/><rect x="22" y="32" width="4" height="5"/><rect x="30" y="32" width="4" height="5"/><rect x="8" y="22" width="4" height="5"/><rect x="8" y="32" width="4" height="5"/><rect x="44" y="22" width="4" height="5"/><rect x="44" y="32" width="4" height="5"/><rect x="24" y="42" width="8" height="10"/></g>
  </svg>
  <h3 class="value-name center-text">Company</h3><div class="value-rule"></div>
  <p class="value-text center-text">Lorem ipsum dolor sit amet acoe ctetur adipiscing elit, sed deiuio dtempaor incididunt ut laboet magna aliqua.</p>
</article>
<article class="value-card" style="left:608px">
  <svg class="value-icon" viewBox="0 0 56 56" fill="#d0201b">
    <polygon points="12,8 44,8 54,20 28,52 2,20"/>
    <g stroke="#fff" stroke-width="2" fill="none"><path d="M2 20 H54"/><path d="M12 8 L20 20 L28 8 L36 20 L44 8"/><path d="M20 20 L28 52 L36 20"/></g>
  </svg>
  <h3 class="value-name center-text">Values</h3><div class="value-rule"></div>
  <p class="value-text center-text">Lorem ipsum dolor sit amet acoe ctetur adipiscing elit, sed deiuio dtempaor incididunt ut laboet magna aliqua.</p>
</article>
<article class="value-card" style="left:857px">
  <svg class="value-icon" viewBox="0 0 56 56" fill="#d0201b">
    <path d="M10 24 a18 18 0 0 1 36 0z"/><rect x="24" y="4" width="8" height="10"/>
    <rect x="6" y="24" width="44" height="5" rx="2"/>
    <path d="M10 32 h36 v6 a8 8 0 0 1-8 8 h-4 l-6-4 l-6 4 h-4 a8 8 0 0 1-8-8z"/>
    <rect x="14" y="35" width="10" height="6" rx="2" fill="#fff"/><rect x="32" y="35" width="10" height="6" rx="2" fill="#fff"/>
  </svg>
  <h3 class="value-name center-text">Safety</h3><div class="value-rule"></div>
  <p class="value-text center-text">Lorem ipsum dolor sit amet acoe ctetur adipiscing elit, sed deiuio dtempaor incididunt ut laboet magna aliqua.</p>
</article>

<!-- Projects -->
<h2 class="section-title center-text" style="top:2586px;font-size:38px">Recent Projects</h2>
<div class="project-photo" style="left:112px;top:2682px;width:313px;height:223px;background:linear-gradient(180deg,#b7b9c9,#7f9a5a 45%,#5a3a28)" role="img" aria-label="Photo of freshly cut sod rows on a graded lawn at sunset"></div>
<div class="project-photo" style="left:444px;top:2682px;width:312px;height:466px;background:linear-gradient(180deg,#aeb3bb,#3d5aa0 50%,#2b2b2b)" role="img" aria-label="Photo of a loader lifting debris into a blue dumpster"></div>
<div class="project-photo" style="left:775px;top:2682px;width:313px;height:223px;background:linear-gradient(160deg,#c9ccd2,#4e6a3e 40%,#3a2e24)" role="img" aria-label="Photo of a tracked loader working soil near pine trees"></div>
<div class="project-photo" style="left:112px;top:2925px;width:313px;height:223px;background:linear-gradient(180deg,#b3b8c0,#9a9070 55%,#6c6250)" role="img" aria-label="Photo of a tracked loader with its telescopic arm raised in a field"></div>
<div class="project-photo" style="left:775px;top:2925px;width:313px;height:223px;background:linear-gradient(180deg,#bcc0c6,#8a8a88 45%,#3c3a38)" role="img" aria-label="Photo of a cleared gravel lot with a blue dumpster"></div>

<!-- Footer -->
<svg class="abs" style="left:0;top:3234px" width="1200" height="511" viewBox="0 0 1200 511">
  <rect x="0" y="0" width="1200" height="511" fill="#121212"/>
  <polygon points="0,12 600,136 1200,12 1200,20 600,156 0,20" fill="#d0201b"/>
</svg>

<div class="footer-brand"><span class="brand-mark" style="width:16px;height:16px"></span>Brovin Terra LLC</div>
<div class="social-box" style="left:150px"><i></i></div>
<div class="social-box" style="left:190px"><i></i></div>
<div class="social-box" style="left:230px"><i></i></div>
<div class="social-box" style="left:270px"><i></i></div>

<h4 class="footer-heading" style="left:416px">Quick Links</h4>
<ul class="footer-list" style="left:416px;top:3490px">
  <li><svg width="14" height="14" viewBox="0 0 14 14"><circle cx="7" cy="7" r="7" fill="#d0201b"/><path d="M4 7h6M7 4l3 3-3 3" stroke="#121212" stroke-width="1.8" fill="none"/></svg>Home</li>
  <li><svg width="14" height="14" viewBox="0 0 14 14"><circle cx="7" cy="7" r="7" fill="#d0201b"/><path d="M4 7h6M7 4l3 3-3 3" stroke="#121212" stroke-width="1.8" fill="none"/></svg>About Us</li>
  <li><svg width="14" height="14" viewBox="0 0 14 14"><circle cx="7" cy="7" r="7" fill="#d0201b"/><path d="M4 7h6M7 4l3 3-3 3" stroke="#121212" stroke-width="1.8" fill="none"/></svg>Our Services</li>
  <li><svg width="14" height="14" viewBox="0 0 14 14"><circle cx="7" cy="7" r="7" fill="#d0201b"/><path d="M4 7h6M7 4l3 3-3 3" stroke="#121212" stroke-width="1.8" fill="none"/></svg>Project</li>
  <li><svg width="14" height="14" viewBox="0 0 14 14"><circle cx="7" cy="7" r="7" fill="#d0201b"/><path d="M4 7h6M7 4l3 3-3 3" stroke="#121212" stroke-width="1.8" fill="none"/></svg>Blog</li>
  <li><svg width="14" height="14" viewBox="0 0 14 14"><circle cx="7" cy="7" r="7" fill="#d0201b"/><path d="M4 7h6M7 4l3 3-3 3" stroke="#121212" stroke-width="1.8" fill="none"/></svg>Contact Us</li>
</ul>

<h4 class="footer-heading" style="left:652px">Other Links</h4>
<ul class="footer-list" style="left:652px;top:3490px">
  <li><svg width="14" height="14" viewBox="0 0 14 14"><circle cx="7" cy="7" r="7" fill="#d0201b"/><path d="M4 7h6M7 4l3 3-3 3" stroke="#121212" stroke-width="1.8" fill="none"/></svg>FAQs</li>
  <li><svg width="14" height="14" viewBox="0 0 14 14"><circle cx="7" cy="7" r="7" fill="#d0201b"/><path d="M4 7h6M7 4l3 3-3 3" stroke="#121212" stroke-width="1.8" fill="none"/></svg>Privacy Policy</li>
  <li><svg width="14" height="14" viewBox="0 0 14 14"><circle cx="7" cy="7" r="7" fill="#d0201b"/><path d="M4 7h6M7 4l3 3-3 3" stroke="#121212" stroke-width="1.8" fill="none"/></svg>Terms Of Use</li>
  <li><svg width="14" height="14" viewBox="0 0 14 14"><circle cx="7" cy="7" r="7" fill="#d0201b"/><path d="M4 7h6M7 4l3 3-3 3" stroke="#121212" stroke-width="1.8" fill="none"/></svg>Legal Support</li>
</ul>

<h4 class="footer-heading" style="left:889px">Contact Us</h4>
<svg class="contact-icon" style="top:3496px" width="12" height="16" viewBox="0 0 12 16"><path d="M6 0a6 6 0 0 1 6 6c0 4-6 10-6 10S0 10 0 6a6 6 0 0 1 6-6z" fill="#d0201b"/><circle cx="6" cy="6" r="2.2" fill="#121212"/></svg>
<p class="contact-line" style="top:3490px">465, Lorum Ipsum Idaho,<br>United States</p>
<svg class="contact-icon" style="top:3558px" width="14" height="14" viewBox="0 0 14 14"><path d="M3 0l3 3-2 2c1 2 3 4 5 5l2-2 3 3-2 3C6 14 0 8 0 3z" fill="#d0201b"/></svg>
<p class="contact-line" style="top:3552px">123 - 456 - 7890</p>
<svg class="contact-icon" style="top:3594px" width="15" height="11" viewBox="0 0 15 11"><rect width="15" height="11" fill="#d0201b"/><path d="M0 0l7.5 6L15 0" stroke="#121212" stroke-width="1.4" fill="none"/></svg>
<p class="contact-line" style="top:3586px">info@brovinterra.com</p>

<div class="footer-rule"></div>
<p class="copyright center-text">© 2021 <b>Brovin <span class="accent">Terra</span> LLC</b>. All Rights Reserved</p>

</body>
</html>
```